Corporate Company Needs 3-series Flyer Template for Print

Flyer Contest Brief - We need a series of 3 templates to market and communicate our company’s leadership development program, using our corporate design elements. All 3 templates should have similar style, color, and elements --- but be noticeably different.

Template #1 – We need one template to communicate the Program Overview. It will include sections such as: learning objectives, descriptions about the online classes, a summary of required project, and the goals and purpose of the program

Template #2 – We need one template to communicate the details of an “Opening Event”. This template should include sections such as: Event location, event time, flight and hotel recommendations, event agenda, etc.

Template #3 - We need one template to communicate the details of an “Closing/Graduation Event”. This template should include sections such as: Event location, event time, flight and hotel recommendations, event agenda, etc.

Usage: We will edit and use the flyers to communicate our program, update information in the flyer and email the flyer to participants with each new class.

Our corporate design elements: Please refer to the attached PowerPoint file that includes a logo for the program, called CLIMB, and the purple brand color used for the program.

Size: Each template should be 8.5 x 11 inches

Look And Feel: Bold, Modern, Professional

File Type: Because I will edit, I need the flyer to be created in Microsoft Publisher or PowerPoint.

About the Program: The program is called CLIMB. It stands for Collaborative Learning In Modern Business. This program is a high profile executive leadership course that lasts for approximately 5 months. Participants attend a live opening event and a live closing / graduation event. Over the course of 5 months the coursework includes: attending online classrooms, regional meetings, e-Learning classes, and manage a project. It is an exclusive program for high profile professional speakers, and it's important for the flyer to be engaging, professional, and clean.

I will need to be able to make small edits back and forth with the successful designer in order to get it just-right. This may only be possibly 2-3 rounds of edits.

Reason: I'm extending the deadline. A few designers have requested this. Thank you.

Target Market(s)

Professional Executive Leaders in my company. Company is Brindlewood Group, USA.

Industry/Entity Type

It Company

Colors
6b449b
0792cd
00a990
add136
fbf289
f04a50

Requirements
Must have
• I must be able to edit all elements of the 3 templates. Therefore, it must be in PowerPoint or Publisher. The designs must use our logo and our purple brand color.
Nice to have
• It would be nice if the designer used the colors provided in the PowerPoint file. It would be nice to see icons used creatively.
Should not have
• Design should not have fancy text or use pictures of people.

```html
<!DOCTYPE html>
<html lang="en">
<head>
<meta charset="utf-8">
<title>CLIMB Opening Event Flyer</title>
<link href="https://fonts.googleapis.com/css2?family=Questrial&display=swap" rel="stylesheet">
<style>
  :root {
    --backdrop: #e6dcc8;
    --paper: #ffffff;
    --band-blue: #4f80bb;
    --brand-purple: #6b449b;
    --ink-dark: #231f20;
    --title-navy: #24457a;
    --body-gray: #4a4a4a;
    --dot-green: #9bd05e;
    --dot-teal: #4ccbc0;
    --dot-pink: #ee1f7c;
    --dot-lavender: #c9c0dc;
    --dot-cyan: #29bfd6;
  }
  html, body {
    margin: 0;
    padding: 0;
    width: 1200px;
    height: 898px;
    overflow: hidden;
    background: var(--backdrop);
    font-family: "Questrial", "Century Gothic", sans-serif;
  }
  .flyer {
    position: absolute;
    left: 275px;
    top: 28px;
    width: 650px;
    height: 842px;
    background: var(--paper);
    box-shadow: 0 6px 24px rgba(0,0,0,0.12);
    text-align: center;
  }
  .top-band {
    height: 40px;
    background: var(--band-blue);
  }
  .program-mark {
    margin-top: 58px;
    display: flex;
    justify-content: center;
    align-items: center;
    gap: 18px;
  }
  .program-square {
    width: 78px;
    height: 78px;
    background: var(--brand-purple);
  }
  .program-name {
    font-size: 112px;
    line-height: 1;
    color: var(--ink-dark);
    letter-spacing: 2px;
  }
  .program-full-name {
    margin-top: 10px;
    font-size: 15px;
    letter-spacing: 0.5px;
    text-transform: uppercase;
    color: var(--brand-purple);
  }
  .event-title {
    margin: 48px auto 0;
    width: 470px;
    color: var(--title-navy);
    font-weight: 400;
    line-height: 1;
  }
  .event-title .line-one {
    display: block;
    font-size: 78px;
    letter-spacing: 1px;
    padding-bottom: 8px;
    border-bottom: 2px solid var(--title-navy);
  }
  .event-title .line-two {
    display: block;
    font-size: 58px;
    padding: 8px 0 10px;
    border-bottom: 2px solid var(--title-navy);
  }
  .event-details {
    margin: 20px auto 0;
    font-size: 29px;
    line-height: 1.28;
    color: var(--body-gray);
  }
  .icon-row {
    position: absolute;
    left: 0;
    right: 0;
    bottom: 60px;
    display: flex;
    justify-content: center;
    gap: 14px;
  }
  .icon-row svg { width: 108px; height: 108px; }
</style>
</head>
<body>
  <main class="flyer">
    <div class="top-band"></div>

    <header class="program-mark">
      <div class="program-square"></div>
      <div class="program-name">CLIMB</div>
    </header>
    <div class="program-full-name">Collaborative Learning In Modern Business</div>

    <h1 class="event-title">
      <span class="line-one">OPENING</span>
      <span class="line-two">EVENT</span>
    </h1>

    <p class="event-details">Event location, event time,<br>flight and hotel<br>recommendations,<br>event agenda, etc.</p>

    <div class="icon-row">
      <svg viewBox="0 0 108 108" aria-label="Progress icon">
        <circle cx="54" cy="54" r="54" fill="var(--dot-green)"/>
        <circle cx="54" cy="54" r="24" fill="none" stroke="#fff" stroke-width="3"/>
        <path d="M54 66 V42 M44 52 L54 42 L64 52" fill="none" stroke="#fff" stroke-width="4" stroke-linecap="round" stroke-linejoin="round"/>
      </svg>
      <svg viewBox="0 0 108 108" aria-label="Idea icon">
        <circle cx="54" cy="54" r="54" fill="var(--dot-teal)"/>
        <circle cx="54" cy="50" r="20" fill="#fff"/>
        <rect x="46" y="66" width="16" height="10" rx="2" fill="#fff"/>
        <rect x="52" y="40" width="4" height="12" fill="var(--dot-teal)"/>
        <rect x="52" y="55" width="4" height="4" fill="var(--dot-teal)"/>
      </svg>
      <svg viewBox="0 0 108 108" aria-label="Network icon">
        <circle cx="54" cy="54" r="54" fill="var(--dot-pink)"/>
        <g stroke="#fff" stroke-width="3">
          <line x1="54" y1="54" x2="54" y2="32"/><line x1="54" y1="54" x2="54" y2="76"/>
          <line x1="54" y1="54" x2="32" y2="54"/><line x1="54" y1="54" x2="76" y2="54"/>
          <line x1="54" y1="54" x2="38" y2="38"/><line x1="54" y1="54" x2="70" y2="70"/>
          <line x1="54" y1="54" x2="70" y2="38"/><line x1="54" y1="54" x2="38" y2="70"/>
        </g>
        <g fill="#fff">
          <circle cx="54" cy="54" r="8"/>
          <circle cx="54" cy="32" r="4"/><circle cx="54" cy="76" r="4"/>
          <circle cx="32" cy="54" r="4"/><circle cx="76" cy="54" r="4"/>
          <circle cx="38" cy="38" r="4"/><circle cx="70" cy="70" r="4"/>
          <circle cx="70" cy="38" r="4"/><circle cx="38" cy="70" r="4"/>
        </g>
      </svg>
      <svg viewBox="0 0 108 108" aria-label="Collaboration icon">
        <circle cx="54" cy="54" r="54" fill="var(--dot-lavender)"/>
        <circle cx="54" cy="54" r="24" fill="none" stroke="#fff" stroke-width="3" stroke-dasharray="6 5"/>
        <circle cx="47" cy="54" r="8" fill="#fff"/>
        <circle cx="61" cy="54" r="8" fill="#fff"/>
      </svg>
      <svg viewBox="0 0 108 108" aria-label="Settings icon">
        <circle cx="54" cy="54" r="54" fill="var(--dot-cyan)"/>
        <g fill="#fff">
          <circle cx="54" cy="54" r="15"/>
          <rect x="50" y="33" width="8" height="42" rx="2"/>
          <rect x="50" y="33" width="8" height="42" rx="2" transform="rotate(45 54 54)"/>
          <rect x="50" y="33" width="8" height="42" rx="2" transform="rotate(90 54 54)"/>
          <rect x="50" y="33" width="8" height="42" rx="2" transform="rotate(135 54 54)"/>
        </g>
        <circle cx="54" cy="54" r="6" fill="var(--dot-cyan)"/>
      </svg>
    </div>
  </main>
</body>
</html>
```